The homepage of a website

This is a simple project that should take from you a few minutes as what is needed is the design of the homepage only, the details are in the attached zip file

Please note that KBLTA board required a special tailored design where they got some parts from the different posted designs, if you are interested please follow the instructions in the below URL and submit your new updated designs as per the instructions (P.S. I will mark the project as guaranteed as an assurance to all of you)

http://quorvanet.com/Projects/KBLTA/Design.jpg

Please note that KBLTA board required a special tailored design where they got some parts from the different posted designs, if you are interested please follow the instructions in the below URL and submit your new updated designs as per the instructions (P.S. I will mark the project as guaranteed as an assurance to all of you) http://quorvanet.com/Projects/KBLTA/Design.jpg

```html
<!DOCTYPE html>
<html lang="en">
<head>
<meta charset="utf-8">
<title>KBLTA – Home</title>
<link href="https://fonts.googleapis.com/css2?family=Lato:wght@400;700&display=swap" rel="stylesheet">
<style>
:root{
  --navy:#1d4a77;
  --navy-dark:#1a4370;
  --orange:#e9572a;
  --orange-dark:#c8441c;
  --text:#333;
  --muted:#666;
  --light:#f1f1f1;
  --line:#d5d5d5;
}
*{box-sizing:border-box;margin:0;padding:0}
html,body{width:1200px;height:2421px;overflow:hidden}
body{font-family:'Lato',sans-serif;color:var(--text);background:#fff;position:relative}
.abs{position:absolute}
.btn{background:var(--orange);color:#fff;border-radius:3px;font-size:13px;display:flex;align-items:center;justify-content:center;border-bottom:2px solid var(--orange-dark)}
/* top bar */
.topbar{top:0;left:0;width:1200px;height:47px;background:#ebebeb}
.header{top:47px;left:0;width:1200px;height:139px;background:#fff}
.brand{left:124px;top:40px;display:flex;align-items:center;gap:14px}
.brand-mark{width:120px;height:120px;border-radius:50%;background:#e8eef5}
.brand-name{font-size:30px;font-weight:700;color:var(--navy)}
.society{right:125px;top:58px;text-align:right;font-size:26px;font-weight:700;color:var(--navy);line-height:1.25}
.search-box{left:857px;top:136px;width:218px;height:32px;border:1px solid var(--line);border-radius:2px;font-size:12px;color:#777;display:flex;align-items:center;justify-content:space-between;padding:0 8px}
/* nav */
.nav{top:186px;left:0;width:1200px;height:53px;background:var(--navy)}
.nav a{position:absolute;top:0;height:53px;line-height:53px;color:#fff;font-size:15px;text-decoration:none;transform:translateX(-50%)}
.nav a.active{background:var(--orange);width:57px;text-align:center}
/* hero */
.hero{top:239px;left:0;width:1200px;height:435px;background:linear-gradient(120deg,#cfe6f3 0%,#8fc3e0 35%,#6aa9cf 60%,#b9d9ec 100%)}
.hero-caption{left:192px;top:437px;width:408px;height:140px;background:rgba(40,80,130,.72);color:#fff;font-size:26px;font-weight:700;line-height:1.3;padding:22px 20px}
/* intro */
.section-title{font-size:23px;color:var(--navy)}
.intro-text{left:123px;top:752px;width:307px;font-size:12.5px;line-height:1.42;text-align:justify}
.poster{left:532px;top:713px;width:218px;height:227px;border:1px solid #ccc;background:linear-gradient(160deg,#f5f1e6,#f3c47c 55%,#d9a34d)}
.cal{left:776px;top:747px;width:259px;border:1px solid var(--orange)}
.cal-head{height:29px;background:var(--orange);color:#fff;font-size:13px;display:flex;align-items:center;justify-content:center;gap:30px}
.cal-grid{display:grid;grid-template-columns:repeat(7,1fr);background:#f3f3f3}
.cal-grid span{height:28.5px;display:flex;align-items:center;justify-content:center;font-size:11px;border-right:1px solid #e2e2e2;border-bottom:1px solid #e2e2e2;position:relative}
.cal-grid .dow{height:16px;font-size:8px;color:#888;background:#f7f7f7}
.cal-grid .ev::after{content:"";position:absolute;bottom:4px;width:4px;height:4px;border-radius:50%;background:#3a9fd6}
.cal-grid .ev2::after{background:#6db33f}
/* features */
.band{top:986px;left:0;width:1200px;height:267px;background:var(--navy)}
.card{top:1022px;width:300px;height:194px;background:#fff;border-radius:3px;text-align:center;padding-top:16px}
.card h3{font-size:19px;font-weight:400;color:var(--navy);margin-top:6px}
.card p{font-size:12px;color:#777;line-height:1.4;margin:6px 22px 0}
/* gallery */
.title-center{width:1200px;left:0;text-align:center}
.title-center .section-title{display:inline-block;border-bottom:1px solid var(--navy);padding:0 2px 3px;position:relative}
.title-center .section-title::after,.col-title::after{content:"";position:absolute;left:50%;bottom:-4px;width:7px;height:7px;margin-left:-3.5px;border-radius:50%;background:var(--navy)}
.photo{top:1332px;width:219px;height:136px;border:1px solid var(--navy);border-radius:2px}
.dots{top:1500px;left:576px;display:flex;gap:6px}
.dots i{width:9px;height:9px;border-radius:50%;background:#aaa}
.dots i:first-child{background:var(--navy)}
/* news */
.news-band{top:1538px;left:0;width:1200px;height:362px;background:var(--light)}
.col-title{position:absolute;font-size:22px;color:var(--navy);border-bottom:1px solid var(--navy);padding-bottom:3px;transform:translateX(-50%);white-space:nowrap}
.item{width:305px;height:100px}
.thumb{position:absolute;left:0;top:0;width:102px;height:100px}
.item h4{position:absolute;left:114px;top:0;font-size:19px;font-weight:400;color:var(--navy)}
.item small{position:absolute;left:114px;top:27px;font-size:11px;color:#666}
.item p{position:absolute;left:114px;top:52px;width:191px;font-size:12px;line-height:1.35;text-align:justify}
.journal{left:776px;top:1623px;width:299px}
.journal h4{font-size:15px;color:var(--navy)}
.journal small{font-size:11px;color:#666}
.journal p{font-size:12.5px;line-height:1.45;text-align:justify;margin-top:18px}
/* partners */
.badge{top:1994px;width:165px;height:79px;border:1px solid #bbb;border-radius:3px;display:flex;align-items:center;justify-content:center}
.badge i{width:60px;height:40px;border-radius:6px;background:#dbe3ec}
/* footer */
.footer{top:2109px;left:0;width:1200px;height:312px;background:var(--navy-dark);color:#fff}
.footer h5{position:absolute;top:30px;font-size:17px;font-weight:700}
.contact-list{position:absolute;left:124px;top:78px;font-size:13px;line-height:23px;list-style:none}
.contact-list li{display:flex;align-items:center;gap:8px}
.socials{position:absolute;left:124px;top:162px;display:flex;gap:22px}
.socials i{width:13px;height:13px;border-radius:50%;background:#fff}
.map{position:absolute;left:369px;top:32px;width:218px;height:166px;background:linear-gradient(135deg,#e9e5dc,#d8d3c6 60%,#f0a94a 61%,#e8e4da 66%)}
.links{position:absolute;left:614px;top:72px;list-style:none;font-size:13px;line-height:21.5px}
.links li::before{content:"»";margin-right:10px}
.signup p{position:absolute;left:776px;top:72px;width:300px;font-size:13px;line-height:23px}
.email{position:absolute;left:776px;top:122px;width:300px;height:38px;background:#fff;border-radius:3px;color:#555;font-size:13px;padding:11px 8px}
.copy{position:absolute;left:0;top:270px;width:1200px;text-align:center;font-size:12.5px}
</style>
</head>
<body>

<div class="abs topbar"></div>
<div class="abs btn" style="left:833px;top:11px;width:68px;height:26px">English ▾</div>
<div class="abs btn" style="left:928px;top:11px;width:62px;height:26px">Login</div>
<div class="abs btn" style="left:1006px;top:11px;width:69px;height:26px">Register</div>

<header class="abs header"></header>
<div class="abs brand"><span class="brand-mark"></span><span class="brand-name">KBLTA</span></div>
<div class="abs society">The Kingsbridge League<br>of Tissue Arts</div>
<div class="abs search-box">Enter Any Keyword
  <svg width="18" height="18" viewBox="0 0 18 18"><circle cx="7.5" cy="7.5" r="5.5" fill="none" stroke="#e9572a" stroke-width="2.5"/><line x1="11.5" y1="11.5" x2="16" y2="16" stroke="#e9572a" stroke-width="3"/></svg>
</div>

<nav class="abs nav">
  <a class="active" style="left:151px">Home</a>
  <a style="left:241px">Board</a>
  <a style="left:335px">History</a>
  <a style="left:438px">Members</a>
  <a style="left:548px">Activities</a>
  <a style="left:645px">Laws</a>
  <a style="left:736px">Journal</a>
  <a style="left:846px">Downloads</a>
  <a style="left:949px">Links</a>
  <a style="left:1040px">Contact</a>
</nav>

<div class="abs hero" role="img" aria-label="Photo of a surgical team in blue scrubs operating"></div>
<div class="abs hero-caption">THE KINGSBRIDGE LEAGUE OF TISSUE ARTS..</div>

<h2 class="abs section-title" style="left:123px;top:706px">Search KBLTA Member</h2>
<p class="abs intro-text">Nertyase riti masertas lertyars asety kertyalicabo nera faes kertyu ersvitae ertyasnemo lasec vaserat niptaide aseoertayse. Basvolernatur aut oditaut. onseqsciunt eque porro quisquam esti doloremuia dolor.Nertyase riti masertas lertyars asety kertyalicabo nera faes kertyu ersvitae ertyasnemo lasec vaserat niptaide aseoertayse. Basvolernatur aut oditaut. onseqsciunt eque porro quisquam esti doloremuia dolor</p>
<div class="abs btn" style="left:123px;top:907px;width:116px;height:33px;font-size:15px">Search</div>
<div class="abs poster" role="img" aria-label="Annual meeting poster with a colourful floral emblem"></div>

<h2 class="abs section-title" style="left:776px;top:706px">Event's Calender</h2>
<div class="abs cal">
  <div class="cal-head"><span>◂</span><span>JAN 2015</span><span>▸</span></div>
  <div class="cal-grid">
    <span class="dow">SUN</span><span class="dow">MON</span><span class="dow">TUE</span><span class="dow">WED</span><span class="dow">THU</span><span class="dow">FRI</span><span class="dow">SAT</span>
    <span>1</span><span class="ev">2</span><span>3</span><span>4</span><span class="ev ev2">5</span><span>6</span><span>7</span>
    <span>8</span><span>9</span><span>10</span><span class="ev ev2">11</span><span>12</span><span>13</span><span>14</span>
    <span>15</span><span>16</span><span>17</span><span>18</span><span class="ev ev2">19</span><span>20</span><span>21</span>
    <span class="ev">22</span><span>23</span><span>24</span><span class="ev ev2">25</span><span>26</span><span>27</span><span>28</span>
    <span>29</span><span>30</span><span>31</span><span></span><span></span><span></span><span></span>
  </div>
</div>

<section class="abs band"></section>
<div class="abs card" style="left:124px">
  <svg width="66" height="60" viewBox="0 0 66 60" fill="#1d4a77"><polygon points="33,2 64,16 2,16"/><rect x="6" y="19" width="54" height="4"/><rect x="10" y="26" width="7" height="22"/><rect x="22" y="26" width="7" height="22"/><rect x="37" y="26" width="7" height="22"/><rect x="49" y="26" width="7" height="22"/><rect x="4" y="51" width="58" height="6"/></svg>
  <h3>Universities</h3>
  <p>Asety kertyalicabo nera Nertyase riti masertas lertya asnemo lasec vaserat nipt aiadefaes kertyu ersvitae erty aseoertayse.</p>
</div>
<div class="abs card" style="left:450px">
  <svg width="66" height="60" viewBox="0 0 66 60" fill="#1d4a77"><circle cx="33" cy="9" r="7"/><circle cx="16" cy="26" r="6"/><circle cx="50" cy="26" r="6"/><path d="M22 28h22v10H22z"/><path d="M4 46c0-8 6-12 12-12s12 4 12 12zM38 46c0-8 6-12 12-12s12 4 12 12z"/><rect x="2" y="48" width="62" height="8"/></svg>
  <h3>E-Learning</h3>
  <p>Asety kertyalicabo nera Nertyase riti masertas lertya asnemo lasec vaserat nipt aiadefaes kertyu ersvitae erty aseoertayse.</p>
</div>
<div class="abs card" style="left:776px">
  <svg width="66" height="60" viewBox="0 0 66 60" fill="none" stroke="#1d4a77" stroke-width="4" stroke-linecap="round"><path d="M14 4v16a12 12 0 0 0 24 0V4"/><path d="M26 32v10a12 12 0 0 0 24 0v-8"/><circle cx="50" cy="26" r="6"/></svg>
  <h3>Patients Eduction</h3>
  <p>Asety kertyalicabo nera Nertyase riti masertas lertya asnemo lasec vaserat nipt aiadefaes kertyu ersvitae erty aseoertayse.</p>
</div>

<div class="abs title-center" style="top:1272px"><h2 class="section-title">Gallery</h2></div>
<div class="abs photo" style="left:124px;background:linear-gradient(135deg,#3e6b8c,#7ea9c4)" role="img" aria-label="Photo of surgeons in an operating theatre"></div>
<div class="abs photo" style="left:369px;background:linear-gradient(135deg,#d9e4ee,#4d8cc4)" role="img" aria-label="Photo of nurses assisting a patient"></div>
<div class="abs photo" style="left:613px;background:linear-gradient(135deg,#9fb8cf,#e2e8ee)" role="img" aria-label="Photo of a doctor visiting a patient in bed"></div>
<div class="abs photo" style="left:857px;background:linear-gradient(135deg,#dfe5ea,#c9b29a)" role="img" aria-label="Photo of a smiling doctor holding a sample"></div>
<div class="abs dots"><i></i><i></i><i></i></div>

<section class="abs news-band"></section>
<h2 class="col-title" style="left:274px;top:1570px">News</h2>
<h2 class="col-title" style="left:599px;top:1570px">Events &amp; upcoming Events</h2>
<h2 class="col-title" style="left:925px;top:1570px">KBLTA Journal</h2>

<div class="abs item" style="left:124px;top:1627px"><div class="thumb" style="background:linear-gradient(135deg,#2f5f86,#9bbfd8)" role="img" aria-label="Photo of a surgical procedure"></div><h4>Lorem Ipsum</h4><small>Posted By 03 Jan 2015</small><p>Praesent vestibulum aenean non-ummy hendrerit mauris. Cum sociis natoque enatibus et magnis</p></div>
<div class="abs item" style="left:124px;top:1756px"><div class="thumb" style="background:linear-gradient(135deg,#4a7391,#b6cddd)" role="img" aria-label="Photo of an operating room team"></div><h4>Lorem Ipsum</h4><small>Posted By 03 Jan 2015</small><p>Praesent vestibulum aenean non-ummy hendrerit mauris. Cum sociis natoque enatibus et magnis</p></div>
<div class="abs item" style="left:450px;top:1627px"><div class="thumb" style="background:linear-gradient(135deg,#6aa39a,#d2e6e1)" role="img" aria-label="Photo of a surgeon in green scrubs"></div><h4>Lorem Ipsum</h4><small>Posted By 03 Jan 2015</small><p>Praesent vestibulum aenean non-ummy hendrerit mauris. Cum sociis natoque enatibus et magnis</p></div>
<div class="abs item" style="left:450px;top:1756px"><div class="thumb" style="background:linear-gradient(135deg,#8fb5d2,#eef2f5)" role="img" aria-label="Photo of surgeons at work"></div><h4>Lorem Ipsum</h4><small>Posted By 03 Jan 2015</small><p>Praesent vestibulum aenean non-ummy hendrerit mauris. Cum sociis natoque enatibus et magnis</p></div>

<div class="abs journal">
  <h4>Publishing Infomation</h4>
  <small>Posted By Jan 2015</small>
  <p>Lorem ipsum dolor sit amet conse ctetur adipisicing elit, sed do eiusmod tempor incididunt ut labore et dolore magna aliqua. Ut enim ad minim veniam, quis nostrud exercitation ullamco laboris nisi ut aliquip ex ea commodo consequat. Lorem ipsum dolor sit amet conse ctetur adipisicing elit,</p>
</div>
<div class="abs btn" style="left:776px;top:1817px;width:124px;height:41px;font-size:15px">View Details</div>

<div class="abs title-center" style="top:1927px"><h2 class="section-title">Gallery</h2></div>
<div class="abs badge" style="left:124px"><i></i></div>
<div class="abs badge" style="left:320px"><i></i></div>
<div class="abs badge" style="left:517px"><i></i></div>
<div class="abs badge" style="left:713px"><i></i></div>
<div class="abs badge" style="left:910px"><i></i></div>

<footer class="abs footer">
  <h5 style="left:124px">Contact Us</h5>
  <ul class="contact-list">
    <li><svg width="12" height="12" viewBox="0 0 12 12" fill="#fff"><path d="M6 1 0 6h2v5h3V8h2v3h3V6h2z"/></svg>41 Marlow Ave Ste 210 Brenton</li>
    <li><svg width="12" height="12" viewBox="0 0 12 12" fill="#fff"><path d="M2 1h3l1 3-2 1a7 7 0 0 0 3 3l1-2 3 1v3c-6 0-10-4-10-10z"/></svg>+12 5550142367</li>
    <li><svg width="12" height="12" viewBox="0 0 12 12"><rect x="0.5" y="2" width="11" height="8" fill="#fff"/><path d="M1 2.5l5 4 5-4" fill="none" stroke="#1a4370"/></svg>hello@kblta-mail.org</li>
  </ul>
  <div class="socials"><i></i><i></i><i></i><i></i><i></i></div>
  <div class="map" role="img" aria-label="Street map showing the office location"></div>
  <h5 style="left:614px">Quick Links</h5>
  <ul class="links"><li>Home</li><li>About us</li><li>Law &amp; Regulation</li><li>Gallery</li><li>News Letter</li><li>Contact</li></ul>
  <h5 style="left:776px">News Latter Signup</h5>
  <div class="signup"><p>Entere Your Email And Subscribe Our Bio Monthy News Lateer</p></div>
  <div class="email">Enter Your Email Address</div>
  <div class="btn" style="position:absolute;left:776px;top:172px;width:93px;height:36px">Subscribe</div>
  <p class="copy">© copyrights KBLTA by KBLTA.com 2015. all right reservds.&nbsp;&nbsp; Privacy Policy</p>
</footer>

</body>
</html>
```